Zielgruppe
Beratung und Coaching von Schulen und Lehrpersonen
Aufgabenstellung
übersichtlich, informativ, beidseitig bedruckt, A5 Format
Ev. ein Bild oder Logo zum Namen: feldweg.lernen, vielleicht ein Bild von einem Schulhauseingang, oder das Schriftzeichen feldweg.lernen gestalten

```html
<!DOCTYPE html>
<html lang="de">
<head>
<meta charset="utf-8">
<title>feldweg.lernen – Flyer A5</title>
<link rel="stylesheet" href="https://fonts.googleapis.com/css2?family=Fira+Sans:wght@400;500;600&display=swap">
<style>
  :root{
    --teal:#009286;
    --ink:#1c1c1c;
    --paper:#ffffff;
    --wood-light:#e6dccd;
    --wood-pale:#efe9e0;
    --wood-mid:#cdbba3;
    --wood-dark:#8e6a48;
    --shirt-green:#2f8f78;
    --folder-red:#e6405f;
    --veil:rgba(236,234,231,.8);
  }
  *{box-sizing:border-box;margin:0;padding:0}
  html,body{width:848px;height:1200px;overflow:hidden;background:var(--paper)}
  body{position:relative;font-family:"Fira Sans",sans-serif;color:var(--ink)}

  .card{position:absolute;left:51px;width:746px;height:526px;overflow:hidden}
  .card--front{top:51px}
  .card--back{top:615px}

  .card__photo{position:absolute;inset:0;
    background:linear-gradient(90deg,
      var(--wood-light) 0%,var(--wood-pale) 28%,var(--wood-mid) 42%,#d9c9b2 53%,
      var(--wood-dark) 55%,var(--shirt-green) 68%,var(--folder-red) 84%,var(--wood-dark) 100%);}
  .card--back .card__photo::after{content:"";position:absolute;inset:0;background:var(--veil)}

  .card__frame{position:absolute;left:26px;top:26px;width:693px;height:472px;border:2.5px solid var(--paper)}

  .headline{position:absolute;left:52px;font-size:22px;line-height:31px;font-weight:400;white-space:nowrap}
  .headline strong{font-weight:500}
  .card--front .headline{top:58px}
  .card--back .headline{top:42px}

  .brand-rule{position:absolute;left:52px;top:433px;width:89px;height:2.5px;background:var(--teal)}
  .brand{position:absolute;left:52px;top:449px;font-size:25px;line-height:30px;font-weight:400}

  .topic{position:absolute;top:87px;width:207px;height:241px;background:var(--paper)}
  .topic--who{left:52px}
  .topic--what{left:269px}
  .topic--why{left:486px}
  .topic__title{margin-top:10px;text-align:center;color:var(--teal);font-size:15px;line-height:18px;font-weight:500;letter-spacing:.4px}
  .topic__list{list-style:none;margin-top:25px}
  .topic__list li{position:relative;font-size:15px;line-height:20px;margin-bottom:10px;white-space:nowrap}
  .topic--who li{padding-left:41px}
  .topic--what li{padding-left:45px}
  .topic--why li{padding-left:44px}
  .tick{position:absolute;top:2px;width:14px;height:16px}
  .topic--who .tick{left:21px}
  .topic--what .tick{left:19px}
  .topic--why .tick{left:17px}
  .topic--why li.two-line .tick{top:12px}

  .contact{position:absolute;left:270px;top:357px;width:423px;height:123px;background:var(--teal);color:var(--paper)}
  .contact__url{text-align:center;font-size:19.5px;line-height:24px;margin-top:10px}
  .contact__person{position:absolute;top:52px;font-size:15px;line-height:17.5px;white-space:nowrap}
  .contact__person strong{font-weight:600}
  .contact__person--left{left:19px}
  .contact__person--right{right:25px;text-align:right}
</style>
</head>
<body>

<section class="card card--front">
  <div class="card__photo" role="img" aria-label="Foto: lächelnde Schülerin mit Kopfhörern, kariertem Hemd und roter Mappe vor Holzwand"></div>
  <div class="card__frame"></div>
  <h1 class="headline"><strong>Unabhängiges Beratungsangebot</strong><br>rund um Bern</h1>
  <div class="brand-rule"></div>
  <p class="brand">feldweg.lernen</p>
</section>

<section class="card card--back">
  <div class="card__photo" role="img" aria-label="Blasses Hintergrundfoto: Schülerin vor Holzwand"></div>
  <div class="card__frame"></div>
  <h2 class="headline"><strong>Unabhängiges Beratungsangebot</strong> rund um Bern</h2>

  <div class="topic topic--who">
    <h3 class="topic__title">FÜR WEN?</h3>
    <ul class="topic__list">
      <li><svg class="tick" viewBox="0 0 14 16"><path d="M1 10 L5 14 C6 9 9 4 13 1" fill="none" stroke="var(--teal)" stroke-width="2.4" stroke-linecap="round"/></svg>Lehrpersonen</li>
      <li><svg class="tick" viewBox="0 0 14 16"><path d="M1 10 L5 14 C6 9 9 4 13 1" fill="none" stroke="var(--teal)" stroke-width="2.4" stroke-linecap="round"/></svg>Heilpädagog*innen</li>
      <li><svg class="tick" viewBox="0 0 14 16"><path d="M1 10 L5 14 C6 9 9 4 13 1" fill="none" stroke="var(--teal)" stroke-width="2.4" stroke-linecap="round"/></svg>Speziallehrpersonen</li>
      <li><svg class="tick" viewBox="0 0 14 16"><path d="M1 10 L5 14 C6 9 9 4 13 1" fill="none" stroke="var(--teal)" stroke-width="2.4" stroke-linecap="round"/></svg>Schulleitungen</li>
    </ul>
  </div>

  <div class="topic topic--what">
    <h3 class="topic__title">FÜR WAS?</h3>
    <ul class="topic__list">
      <li><svg class="tick" viewBox="0 0 14 16"><path d="M1 10 L5 14 C6 9 9 4 13 1" fill="none" stroke="var(--teal)" stroke-width="2.4" stroke-linecap="round"/></svg>Beratung</li>
      <li><svg class="tick" viewBox="0 0 14 16"><path d="M1 10 L5 14 C6 9 9 4 13 1" fill="none" stroke="var(--teal)" stroke-width="2.4" stroke-linecap="round"/></svg>Coaching</li>
      <li><svg class="tick" viewBox="0 0 14 16"><path d="M1 10 L5 14 C6 9 9 4 13 1" fill="none" stroke="var(--teal)" stroke-width="2.4" stroke-linecap="round"/></svg>Supervision</li>
      <li><svg class="tick" viewBox="0 0 14 16"><path d="M1 10 L5 14 C6 9 9 4 13 1" fill="none" stroke="var(--teal)" stroke-width="2.4" stroke-linecap="round"/></svg>Begleitung</li>
      <li><svg class="tick" viewBox="0 0 14 16"><path d="M1 10 L5 14 C6 9 9 4 13 1" fill="none" stroke="var(--teal)" stroke-width="2.4" stroke-linecap="round"/></svg>Weiterbildung</li>
    </ul>
  </div>

  <div class="topic topic--why">
    <h3 class="topic__title">WOZU?</h3>
    <ul class="topic__list">
      <li><svg class="tick" viewBox="0 0 14 16"><path d="M1 10 L5 14 C6 9 9 4 13 1" fill="none" stroke="var(--teal)" stroke-width="2.4" stroke-linecap="round"/></svg>Aufgaben- und</li>
      <li><svg class="tick" viewBox="0 0 14 16"><path d="M1 10 L5 14 C6 9 9 4 13 1" fill="none" stroke="var(--teal)" stroke-width="2.4" stroke-linecap="round"/></svg>Rollenklärung</li>
      <li class="two-line"><svg class="tick" viewBox="0 0 14 16"><path d="M1 10 L5 14 C6 9 9 4 13 1" fill="none" stroke="var(--teal)" stroke-width="2.4" stroke-linecap="round"/></svg>Optimierung der<br>Zusammenarbeit</li>
      <li><svg class="tick" viewBox="0 0 14 16"><path d="M1 10 L5 14 C6 9 9 4 13 1" fill="none" stroke="var(--teal)" stroke-width="2.4" stroke-linecap="round"/></svg>Beratung bei intSoS</li>
      <li><svg class="tick" viewBox="0 0 14 16"><path d="M1 10 L5 14 C6 9 9 4 13 1" fill="none" stroke="var(--teal)" stroke-width="2.4" stroke-linecap="round"/></svg>Reflexion</li>
    </ul>
  </div>

  <div class="contact">
    <p class="contact__url">www.feldweg.lernen</p>
    <p class="contact__person contact__person--left"><strong>Andrea Lina Brunner</strong><br>a.brunner@feldweg.lernen<br>078 555 12 34</p>
    <p class="contact__person contact__person--right"><strong>Sandra Keller</strong><br>s.keller@feldweg.lernen<br>079 555 43 21</p>
  </div>

  <div class="brand-rule"></div>
  <p class="brand">feldweg.lernen</p>
</section>

</body>
</html>
```